Printing Business Card

I would like the colorful accents of my business to match with an artistic design. The idea is that I would like to have a creative mix so that I am making a embossed, suede card to show off with marketing events.

```html
<!DOCTYPE html>
<html lang="en">
<head>
<meta charset="UTF-8">
<title>Keystone Print Co. – Business Card</title>
<link href="https://fonts.googleapis.com/css2?family=Oswald:wght@600&family=Work+Sans:wght@400;600&display=swap" rel="stylesheet">
<style>
  :root {
    --backdrop: #d9d9d9;
    --card-white: #ffffff;
    --ink: #1b1b1b;
    --cyan: #0c94e2;
    --magenta: #e0157f;
    --yellow: #f5c200;
    --muted: #444444;
  }
  * { box-sizing: border-box; margin: 0; padding: 0; }
  html, body { width: 1200px; height: 800px; overflow: hidden; }
  body {
    background: var(--backdrop);
    font-family: "Work Sans", sans-serif;
    display: flex;
    align-items: center;
    justify-content: center;
    gap: 40px;
  }
  .card {
    position: relative;
    width: 525px;
    height: 300px;
    border-radius: 22px;
    overflow: hidden;
    box-shadow: 0 6px 18px rgba(0,0,0,0.18);
  }
  .card--front { background: var(--card-white); }
  .card--back {
    background: var(--cyan);
    display: flex;
    align-items: center;
    justify-content: center;
  }

  .brand {
    display: flex;
    align-items: center;
    gap: 10px;
    font-family: "Work Sans", sans-serif;
    font-weight: 600;
    color: var(--ink);
  }
  .brand__dot {
    width: 18px; height: 18px; border-radius: 50%;
    background: var(--cyan);
  }
  .card--front .brand {
    position: absolute;
    top: 52px; right: 40px;
    font-size: 24px;
  }
  .card--back .brand { font-size: 36px; color: var(--card-white); }
  .card--back .brand__dot { width: 26px; height: 26px; background: var(--card-white); }

  .person {
    position: absolute;
    left: 36px; bottom: 96px;
  }
  .person__name {
    font-family: "Oswald", sans-serif;
    font-weight: 600;
    font-size: 24px;
    letter-spacing: 0.5px;
    color: var(--ink);
    line-height: 1.1;
  }
  .person__role {
    font-size: 13px;
    color: var(--cyan);
    letter-spacing: 0.5px;
  }

  .rule {
    position: absolute;
    left: 36px; right: 36px; bottom: 86px;
    height: 1px;
    background: var(--ink);
  }

  .contacts {
    position: absolute;
    left: 36px; top: 222px;
    list-style: none;
    font-size: 12.5px;
    color: var(--muted);
    line-height: 20px;
  }
  .contacts li { display: flex; align-items: center; gap: 8px; }
  .contacts svg { width: 11px; height: 11px; flex: none; }

  .address {
    position: absolute;
    right: 36px; bottom: 96px;
    text-align: right;
    font-size: 12.5px;
    line-height: 17px;
    color: var(--muted);
  }
  .address strong { font-weight: 600; color: var(--ink); }

  .ink-bars {
    position: absolute;
    right: 60px; bottom: 0;
    display: flex;
  }
  .ink-bars span { width: 44px; height: 8px; }
  .ink-bars .c { background: var(--cyan); }
  .ink-bars .m { background: var(--magenta); }
  .ink-bars .y { background: var(--yellow); }
</style>
</head>
<body>
  <section class="card card--front" aria-label="Card front">
    <div class="brand"><span class="brand__dot"></span>Keystone Print Co.</div>

    <div class="person">
      <h1 class="person__name">DANIEL REYES</h1>
      <p class="person__role">President</p>
    </div>

    <div class="rule"></div>

    <ul class="contacts">
      <li>
        <svg viewBox="0 0 12 12"><path d="M3 1 L5 3.5 L4 5 Q5.5 7.5 7 8 L8.5 7 L11 9 L9.5 11 Q4 10.5 1 3 Z" fill="var(--cyan)"/></svg>
        555-014-2290
      </li>
      <li>
        <svg viewBox="0 0 12 12"><rect x="1.5" y="1.5" width="9" height="9" fill="none" stroke="var(--magenta)" stroke-width="1.8"/></svg>
        555-017-3864
      </li>
      <li>
        <svg viewBox="0 0 12 12"><rect x="0.5" y="2" width="11" height="8" fill="var(--yellow)"/><path d="M0.5 2 L6 6.5 L11.5 2" fill="none" stroke="#fff" stroke-width="1"/></svg>
        hello@keystoneprint.com
      </li>
    </ul>

    <address class="address" style="font-style: normal;">
      1420 Harbor View Road<br>
      Juneau, Alaska 99801<br>
      www.<strong>keystoneprint</strong>.com
    </address>

    <div class="ink-bars"><span class="c"></span><span class="m"></span><span class="y"></span></div>
  </section>

  <section class="card card--back" aria-label="Card back">
    <div class="brand"><span class="brand__dot"></span>Keystone Print Co.</div>
  </section>
</body>
</html>
```